Web Design for an Online Dating Web Site

We need an uncoded web design for a new online dating web site called zMatchy.net. Simplicity and boldness are the key factors in the successful design.
Please look at the requirements document attached for details.
Updates
Dear all,
Please AVOID USING A PICTURE OF A HAPPY COUPLE ON THE HOME PAGE of the site. We highly want to move away from this space as it makes our web site just like another dating web site.
We like something simple with web 2.0 look and feel. The examples in the Requirements Document are exactly the design we are after.
Regards
Tarn
Industry/Entity Type
Dating
Look and feel
Each slider illustrates characteristics of the customer's brand and the style your logo design should communicate.

```html
<!DOCTYPE html>
<html lang="en">
<head>
<meta charset="utf-8">
<title>zMatchy.net – My Messages</title>
<link href="https://fonts.googleapis.com/css2?family=PT+Sans:wght@400;700&display=swap" rel="stylesheet">
<style>
:root{
  --pink:#e0177f;
  --pink-soft:#f16aae;
  --ink:#333;
  --grey-text:#555;
  --page:#f4f4f4;
  --panel:#e2e2e2;
  --panel-line:#cfcfcf;
  --header-top:#8a8a8a;
  --header-a:#e9e9e9;
  --header-b:#a9a9a9;
  --footer-a:#3a3a3a;
  --footer-b:#1f1f1f;
  --field:#6e6e6e;
  --white:#fff;
}
*{box-sizing:border-box;margin:0;padding:0}
html,body{width:880px;height:1200px;overflow:hidden}
body{position:relative;background:var(--page);font-family:"PT Sans",Arial,sans-serif;color:var(--ink)}
.abs{position:absolute}

/* header */
.site-header{left:0;top:0;width:880px;height:117px;background:linear-gradient(#d2d2d2 0,var(--header-a) 12px,var(--header-b) 117px);border-top:11px solid var(--header-top)}
.brand{left:73px;top:30px;display:flex;flex-direction:column}
.brand-name{font-size:50px;font-weight:700;color:var(--pink);line-height:1;letter-spacing:-1px}
.brand-url{font-size:10px;color:#555;align-self:flex-end;margin-top:-4px}
.header-wedge{left:0;top:117px}

.main-nav{left:368px;top:79px;display:flex;gap:3px}
.nav-item{font-size:12px;padding:2px 5px;border:1px solid #777;border-radius:5px;background:linear-gradient(#fafafa,#cfcfcf);color:#222;line-height:14px}
.nav-item.is-active{background:linear-gradient(#777,#444);color:var(--white);border-color:#333}

.dropdown{left:359px;top:107px;width:121px;height:104px;background:var(--white);border-radius:4px;box-shadow:0 1px 4px rgba(0,0,0,.45);padding:10px 0 0}
.dropdown::before{content:"";position:absolute;left:12px;top:-6px;border:6px solid transparent;border-top:0;border-bottom-color:var(--white)}
.dropdown-item{display:flex;align-items:center;gap:7px;font-size:8px;height:17px;padding-left:13px;color:#333}
.dropdown-item.is-current{background:var(--pink-soft);color:var(--white)}
.dd-icon{width:11px;height:9px;background:#333;border-radius:1px}

/* messages panel */
.panel{left:71px;top:184px;width:740px;height:560px;background:var(--panel);border:1px solid var(--panel-line);border-radius:6px}
.panel-title{left:111px;top:202px;font-size:17px;color:var(--pink);font-weight:400}
.panel-intro{left:111px;top:233px;width:640px;font-size:8px;line-height:10px;color:#333}

.message{left:72px;width:738px;height:50px}
.message.is-hover{background:#f6f6f6;border:1px solid #bbb}
.avatar{left:39px;top:0;width:40px;height:40px;border-radius:4px;border:1px solid #888;background:linear-gradient(#9a9a9a,#6c6c6c)}
.avatar.photo{background:linear-gradient(#c9a880,#8d6f55)}
.msg-date{left:97px;top:0;font-size:8px;color:#333}
.msg-new{color:var(--pink);font-size:6px;margin-left:6px;font-weight:700}
.msg-text{left:97px;top:12px;font-size:7px;color:#333;white-space:nowrap}
.msg-tools{left:97px;top:24px;display:flex;gap:5px;align-items:center}
.bin{width:7px;height:8px;border:1.5px solid #222;border-top-width:2.5px}

/* footer */
.site-footer{left:0;top:796px;width:880px;height:404px;background:radial-gradient(circle at 470px 300px,#444 0,#333 220px,var(--footer-b) 221px,#2a2a2a 420px)}
.footer-notch{left:36px;top:796px}
.footer-col{top:857px}
.footer-heading{font-size:17px;color:var(--pink);font-weight:400;margin-bottom:7px}
.footer-links{list-style:none;font-size:8px;line-height:10.5px;color:var(--white)}
.social{display:grid;grid-template-columns:repeat(3,16px);gap:13px 22px;margin-top:4px}
.social-dot{width:16px;height:16px;border-radius:50%;background:#cfcfcf}
.share-row{display:flex;gap:14px}
.share{display:flex;flex-direction:column;align-items:center;width:35px}
.share-count{width:35px;height:20px;background:var(--white);border:1px solid #999;border-radius:2px;font-size:11px;color:#222;text-align:center;line-height:18px}
.share-btn{margin-top:3px;width:35px;height:11px;background:#5d7ab0;color:var(--white);font-size:7px;text-align:center;line-height:11px;border-radius:2px}
.share-btn.sky{background:#a9d4ee;color:#1d5a86}
.share-btn.green{background:#e5e5e5;color:#2a7a2a;width:30px}
.share.small .share-count{width:30px;height:17px;line-height:15px;font-size:9px}
.field{width:140px;height:23px;background:var(--field);border-radius:4px;font-size:8px;color:#ddd;padding:6px 9px;margin-bottom:8px}
.field.comments{width:208px;height:104px}
.send-btn{width:96px;height:27px;background:#222;border:1px solid #888;border-radius:5px;color:var(--pink);font-size:8px;text-align:center;line-height:25px;margin-top:12px}
.footer-brand{left:0;width:880px;top:1130px;text-align:center}
.footer-brand .brand-name{font-size:40px;color:#141414}
.footer-brand .brand-url{display:block;font-size:9px;color:#999;margin-left:80px;margin-top:-4px}
</style>
</head>
<body>

<header class="abs site-header"></header>
<div class="abs brand"><span class="brand-name">zMatchy</span><span class="brand-url">zmatchy.net</span></div>
<svg class="abs header-wedge" width="134" height="58" viewBox="0 0 134 58" aria-hidden="true">
  <path d="M0 0H134C100 6 84 18 72 58C62 20 40 8 0 10Z" fill="var(--pink)"/>
</svg>

<nav class="abs main-nav">
  <span class="nav-item is-active">My Stuff</span>
  <span class="nav-item">My Messages</span>
  <span class="nav-item">Start Dating</span>
  <span class="nav-item">Sign Out</span>
  <span class="nav-item">Help</span>
</nav>
<div class="abs dropdown">
  <div class="dropdown-item is-current"><span class="dd-icon"></span>My Details</div>
  <div class="dropdown-item"><span class="dd-icon"></span>My Seeking Criteria</div>
  <div class="dropdown-item"><span class="dd-icon"></span>My Avatar</div>
  <div class="dropdown-item"><span class="dd-icon"></span>My Video</div>
  <div class="dropdown-item"><span class="dd-icon"></span>My Friends</div>
</div>

<main>
  <div class="abs panel"></div>
  <h1 class="abs panel-title">My Messages</h1>
  <p class="abs panel-intro">Lorem ipsum dolor sit amet, et omittam insolens duo, movet repudiare his ad. Pri eu coplosae epicurei accommodare, facilis voluptatum delicatissimi duo et. Elitr viderer prodesset te sed, pri no quot ignota expicari, autem praesent te mel. Eam clita hendrerit ei. Amet quando referrentur eu pri.</p>

  <div class="abs message" style="top:268px"><div class="abs avatar" role="img" aria-label="Member silhouette placeholder"></div><div class="abs msg-date">JUL 27, 2011<span class="msg-new">New</span></div><div class="abs msg-text">Lorem ipsum dolor sit amet, et omittam insolens duo, movet repudiare his ad. Pri eu coplosae epicurei accommodare, facilis voluptatum delicatissimi duo ...</div><div class="abs msg-tools"><span class="bin"></span><svg width="9" height="8" viewBox="0 0 9 8"><path d="M1 4l2.5 3L8 1" stroke="var(--pink)" stroke-width="1.6" fill="none"/></svg></div></div>
  <div class="abs message" style="top:318px"><div class="abs avatar" role="img" aria-label="Member silhouette placeholder"></div><div class="abs msg-date">JUL 27, 2011</div><div class="abs msg-text">Lorem ipsum dolor sit amet, et omittam insolens duo, movet repudiare his ad. Pri eu coplosae epicurei accommodare, facilis voluptatum delicatissimi duo ...</div><div class="abs msg-tools"><span class="bin"></span><svg width="9" height="8" viewBox="0 0 9 8"><path d="M1 4l2.5 3L8 1" stroke="#222" stroke-width="1.6" fill="none"/></svg></div></div>
  <div class="abs message" style="top:368px"><div class="abs avatar photo" role="img" aria-label="Member profile photo"></div><div class="abs msg-date">JUL 27, 2011</div><div class="abs msg-text">Lorem ipsum dolor sit amet, et omittam insolens duo, movet repudiare his ad. Pri eu coplosae epicurei accommodare, facilis voluptatum delicatissimi duo ...</div><div class="abs msg-tools"><span class="bin"></span><svg width="9" height="8" viewBox="0 0 9 8"><path d="M1 4l2.5 3L8 1" stroke="#222" stroke-width="1.6" fill="none"/></svg></div></div>
  <div class="abs message is-hover" style="top:416px;height:52px;padding-top:10px"><div class="abs avatar" style="top:9px" role="img" aria-label="Member silhouette placeholder"></div><div class="abs msg-date" style="top:9px">JUL 27, 2011</div><div class="abs msg-text" style="top:21px">Lorem ipsum dolor sit amet, et omittam insolens duo, movet repudiare his ad. Pri eu coplosae epicurei accommodare, facilis voluptatum delicatissimi duo ...</div><div class="abs msg-tools" style="top:33px"><span class="bin"></span><svg width="9" height="8" viewBox="0 0 9 8"><path d="M1 4l2.5 3L8 1" stroke="#222" stroke-width="1.6" fill="none"/></svg></div></div>
  <div class="abs message" style="top:474px"><div class="abs avatar" role="img" aria-label="Member silhouette placeholder"></div><div class="abs msg-date">JUL 27, 2011</div><div class="abs msg-text">Lorem ipsum dolor sit amet, et omittam insolens duo, movet repudiare his ad. Pri eu coplosae epicurei accommodare, facilis voluptatum delicatissimi duo ...</div><div class="abs msg-tools"><span class="bin"></span><svg width="9" height="8" viewBox="0 0 9 8"><path d="M1 4l2.5 3L8 1" stroke="#222" stroke-width="1.6" fill="none"/></svg></div></div>
  <div class="abs message" style="top:523px"><div class="abs avatar" role="img" aria-label="Member silhouette placeholder"></div><div class="abs msg-date">JUL 27, 2011</div><div class="abs msg-text">Lorem ipsum dolor sit amet, et omittam insolens duo, movet repudiare his ad. Pri eu coplosae epicurei accommodare, facilis voluptatum delicatissimi duo ...</div><div class="abs msg-tools"><span class="bin"></span><svg width="9" height="8" viewBox="0 0 9 8"><path d="M1 4l2.5 3L8 1" stroke="#222" stroke-width="1.6" fill="none"/></svg></div></div>
  <div class="abs message" style="top:573px"><div class="abs avatar photo" role="img" aria-label="Member profile photo"></div><div class="abs msg-date">JUL 27, 2011</div><div class="abs msg-text">Lorem ipsum dolor sit amet, et omittam insolens duo, movet repudiare his ad. Pri eu coplosae epicurei accommodare, facilis voluptatum delicatissimi duo ...</div><div class="abs msg-tools"><span class="bin"></span><svg width="9" height="8" viewBox="0 0 9 8"><path d="M1 4l2.5 3L8 1" stroke="#222" stroke-width="1.6" fill="none"/></svg></div></div>
  <div class="abs message" style="top:623px"><div class="abs avatar" role="img" aria-label="Member silhouette placeholder"></div><div class="abs msg-date">JUL 27, 2011</div><div class="abs msg-text">Lorem ipsum dolor sit amet, et omittam insolens duo, movet repudiare his ad. Pri eu coplosae epicurei accommodare, facilis voluptatum delicatissimi duo ...</div><div class="abs msg-tools"><span class="bin"></span><svg width="9" height="8" viewBox="0 0 9 8"><path d="M1 4l2.5 3L8 1" stroke="#222" stroke-width="1.6" fill="none"/></svg></div></div>
</main>

<footer>
  <div class="abs site-footer"></div>
  <svg class="abs footer-notch" width="76" height="42" viewBox="0 0 76 42" aria-hidden="true">
    <path d="M0 0H76C56 4 44 14 38 42C32 14 20 4 0 0Z" fill="var(--page)"/>
  </svg>

  <div class="abs footer-col" style="left:72px">
    <h2 class="footer-heading">Read More</h2>
    <ul class="footer-links"><li>Why zMatchy</li><li>How it works</li><li>Sign Up</li><li>Login</li><li>About Us</li></ul>
  </div>
  <div class="abs footer-col" style="left:236px">
    <h2 class="footer-heading">Find us on</h2>
    <div class="social"><span class="social-dot"></span><span class="social-dot"></span><span class="social-dot"></span><span class="social-dot"></span></div>
  </div>
  <div class="abs footer-col" style="left:420px">
    <h2 class="footer-heading">Do u Like us</h2>
    <div class="share-row">
      <div class="share"><div class="share-count">220</div><div class="share-btn">Share</div></div>
      <div class="share"><div class="share-count" style="color:#2a6a9a;font-size:9px">6,314</div><div class="share-btn sky">Post</div></div>
    </div>
    <div class="share small" style="margin-top:12px;width:30px"><div class="share-count">1</div><div class="share-btn green">Like</div></div>
  </div>
  <div class="abs footer-col" style="left:603px">
    <h2 class="footer-heading">Let's Talk</h2>
    <div class="field">Name</div>
    <div class="field">E-mail</div>
    <div class="field comments">Comments</div>
    <div class="send-btn">Send</div>
  </div>

  <div class="abs footer-brand"><span class="brand-name">zMatchy</span><span class="brand-url">zmatchy.net</span></div>
</footer>

</body>
</html>
```